Mortgage Loan officer needs clean/modern business card design

Looking for a clean, modern 2-sided business card design. We like the earth tones used in our logo and website http://vukarhome-lending.example . Would also like to incorporate: 1) Something special to make our card stand out - a pop of color or embossed logo, for instance and 2) please include "Mortgage Loans" "Reverse Mortgages" "Private Money Loans" on back of card with the logo.

Front: Needs to include agent/company license info - see website. Agent name: Niall Hargrove

Here are fonts and colors used for our logo:
Font: Avenir Next
Colors:
#2c3539 - Dark Gray
#576870 - Light Gray
#ffffff - Background White

Target Market(s)

Prospects and current clients. Will also be distributing to people in professional network (attorneys and CPAs)

Industry/Entity Type

Business

Contact Information for Business Card

Include agent name, contact info, website on front, licensing info for agent an company. Logo and services offered on back

Font styles to use
Other font styles liked:
• Avenir Next

Requirements
Must have
• See project description
Should not have
• Nothing cheesy

```html
<!DOCTYPE html>
<html lang="en">
<head>
<meta charset="utf-8">
<title>Vukar Home Lending – Business Card</title>
<link rel="stylesheet" href="https://fonts.googleapis.com/css2?family=Nunito+Sans:wght@400;600&display=swap">
<style>
  :root {
    --dark-gray: #2c3539;
    --light-gray: #576870;
    --card-white: #f6f6f6;
    --backdrop: #e6e6e6;
    --text: #3a4246;
  }
  * { margin: 0; padding: 0; box-sizing: border-box; }
  html, body { width: 1200px; height: 576px; overflow: hidden; }
  body {
    background: var(--backdrop);
    font-family: "Nunito Sans", Arial, sans-serif;
    color: var(--text);
    position: relative;
  }
  .card {
    position: absolute;
    top: 139px;
    width: 484px;
    height: 292px;
    background: var(--card-white);
    border-radius: 12px;
    overflow: hidden;
  }
  .card--back { left: 82px; }
  .card--front { left: 602px; }

  .brand-circle {
    position: absolute;
    border: 1.5px solid var(--dark-gray);
    border-radius: 50%;
    display: flex;
    align-items: center;
    justify-content: center;
    text-align: center;
  }
  .brand-name {
    font-weight: 400;
    font-size: 17px;
    line-height: 1.3;
    color: var(--light-gray);
  }
  .card--back .brand-circle { left: 160px; top: 47px; width: 164px; height: 164px; }
  .card--front .brand-circle { left: 37px; top: 58px; width: 168px; height: 168px; }

  .services-band {
    position: absolute;
    left: 0; right: 0;
    top: 248px;
    height: 25px;
    background: var(--dark-gray);
    color: #eef0f1;
    font-size: 12.5px;
    display: flex;
    align-items: center;
    justify-content: center;
    gap: 7px;
  }

  .wave { position: absolute; inset: 0; width: 100%; height: 100%; }

  .agent {
    position: absolute;
    right: 26px;
    top: 26px;
    text-align: right;
    color: #ffffff;
  }
  .agent-name { font-size: 19px; font-weight: 600; line-height: 1.1; }
  .agent-title { font-size: 10.5px; margin-top: 3px; }

  .contact {
    position: absolute;
    right: 26px;
    top: 188px;
    list-style: none;
    text-align: right;
    font-size: 10.5px;
  }
  .contact li { height: 18px; display: flex; align-items: center; justify-content: flex-end; gap: 6px; }
  .contact li.address { margin-bottom: 7px; padding-right: 0; }
  .contact svg { width: 11px; height: 11px; fill: var(--light-gray); }

  .license {
    position: absolute;
    left: 50px;
    top: 252px;
    font-size: 12.5px;
    letter-spacing: 0.2px;
  }
</style>
</head>
<body>

  <section class="card card--back">
    <div class="brand-circle"><span class="brand-name">Vukar Home<br>Lending</span></div>
    <div class="services-band">
      <span>Mortgage Loans</span><span>|</span><span>Reverse Mortgages</span><span>|</span><span>Private Money Loans</span>
    </div>
  </section>

  <section class="card card--front">
    <svg class="wave" viewBox="0 0 600 363" preserveAspectRatio="none" aria-hidden="true">
      <path fill="var(--dark-gray)" d="M0,0 H600 V136 C520,140 455,120 395,88 C320,45 230,18 0,24 Z"/>
      <path fill="var(--light-gray)" d="M0,42 C150,14 300,34 400,104 C460,140 530,150 600,150 V160 C520,162 450,150 388,116 C300,58 150,38 0,64 Z"/>
      <path fill="var(--light-gray)" d="M60,52 C160,36 250,40 330,62 C250,48 160,46 60,52 Z"/>
    </svg>

    <div class="agent">
      <div class="agent-name">Niall Hargrove</div>
      <div class="agent-title">Owner/Director</div>
    </div>

    <div class="brand-circle"><span class="brand-name">Vukar Home<br>Lending</span></div>

    <ul class="contact">
      <li class="address">27 Harbour Lane, Avalon NSW 2107</li>
      <li>0400 555 018
        <svg viewBox="0 0 12 12" aria-hidden="true"><path d="M1,4 C1,2 3,1.5 6,1.5 S11,2 11,4 V5 H8.5 V3.8 H3.5 V5 H1 Z M3,6 H9 L10.5,10.5 H1.5 Z"/></svg>
      </li>
      <li>www.vukarhome-lending.example
        <svg viewBox="0 0 12 12" aria-hidden="true"><circle cx="6" cy="6" r="5" fill="none" stroke="var(--light-gray)" stroke-width="1.2"/><path d="M1,6 H11 M6,1 C3,4 3,8 6,11 C9,8 9,4 6,1" fill="none" stroke="var(--light-gray)" stroke-width="1"/></svg>
      </li>
      <li>niall.hargrove@vukarhome-lending.example
        <svg viewBox="0 0 12 12" aria-hidden="true"><path d="M1,2.5 H11 V9.5 H1 Z" /><path d="M1,2.5 L6,6.5 L11,2.5" fill="none" stroke="#f6f6f6" stroke-width="1"/></svg>
      </li>
    </ul>

    <div class="license">LICANSE NO.: 12345678</div>
  </section>

</body>
</html>
```